Business cards design for T38 (Разработка визитных карточек)

We would like to get design of our business cards loosely based on our website design [url removed, login to view]

logo in vector is atteched

There should be following info to be present on business card:
Martin Colvey
CEO
T38
+7 (222) 222-22-22
+7 (222) 222-22-22
colvey@tessarine-mail.ru
222222, Moscow, Ulitsa Tikhvoronskaya, 7B

```html
<!DOCTYPE html>
<html lang="en">
<head>
<meta charset="utf-8">
<title>T38 — Business Card</title>
<link rel="stylesheet" href="https://fonts.googleapis.com/css2?family=Open+Sans:wght@400&family=Tinos&display=swap">
<style>
  :root {
    --red-deep: #5e0408;
    --red-mid: #a3141b;
    --red-glow: #d0262c;
    --silver-light: #ffffff;
    --silver-mid: #b9bcc0;
    --steel: #6e7277;
    --carbon: #2a2c2f;
    --carbon-dark: #141517;
    --text-light: #ffffff;
  }
  html, body {
    margin: 0;
    padding: 0;
    width: 1200px;
    height: 695px;
    overflow: hidden;
    background: #ffffff;
  }
  .card {
    position: relative;
    width: 1200px;
    height: 695px;
    overflow: hidden;
    background: radial-gradient(ellipse 70% 80% at 50% 35%, var(--red-glow) 0%, var(--red-mid) 45%, var(--red-deep) 100%);
  }
  .card__swoosh {
    position: absolute;
    inset: 0;
    width: 1200px;
    height: 695px;
  }
  .card__name {
    position: absolute;
    top: 52px;
    left: 0;
    width: 100%;
    margin: 0;
    text-align: center;
    font-family: "Tinos", "Times New Roman", serif;
    font-weight: 400;
    font-size: 98px;
    line-height: 1;
    letter-spacing: 1px;
    color: var(--text-light);
    text-transform: uppercase;
    text-shadow: 0 2px 4px rgba(0,0,0,0.45);
  }
  .card__role {
    position: absolute;
    top: 190px;
    left: 0;
    width: 100%;
    margin: 0;
    text-align: center;
    font-family: "Tinos", "Times New Roman", serif;
    font-weight: 400;
    font-size: 66px;
    line-height: 1;
    color: var(--text-light);
    text-shadow: 0 2px 4px rgba(0,0,0,0.45);
  }
  .card__contacts {
    position: absolute;
    top: 318px;
    left: 83px;
    margin: 0;
    padding: 0;
    list-style: none;
    font-family: "Open Sans", Arial, sans-serif;
    font-size: 34px;
    line-height: 54px;
    color: var(--text-light);
    text-shadow: 0 1px 3px rgba(0,0,0,0.6);
  }
  .card__brand {
    position: absolute;
    right: 93px;
    top: 520px;
    margin: 0;
    font-family: "Open Sans", Arial, sans-serif;
    font-weight: 400;
    font-size: 110px;
    line-height: 1;
    color: var(--text-light);
  }
</style>
</head>
<body>
  <div class="card">
    <svg class="card__swoosh" viewBox="0 0 1200 695" aria-hidden="true">
      <defs>
        <linearGradient id="carbonFill" x1="0" y1="0" x2="0" y2="1">
          <stop offset="0" stop-color="var(--carbon)"/>
          <stop offset="1" stop-color="var(--carbon-dark)"/>
        </linearGradient>
        <linearGradient id="silverFill" x1="0" y1="0" x2="1" y2="0">
          <stop offset="0" stop-color="var(--silver-light)"/>
          <stop offset="0.5" stop-color="var(--silver-mid)"/>
          <stop offset="1" stop-color="var(--silver-light)"/>
        </linearGradient>
        <linearGradient id="steelFill" x1="0" y1="0" x2="0" y2="1">
          <stop offset="0" stop-color="var(--steel)"/>
          <stop offset="1" stop-color="var(--carbon)"/>
        </linearGradient>
      </defs>
      <path d="M0,420 C300,455 700,430 1200,355 L1200,695 L0,695 Z" fill="url(#silverFill)"/>
      <path d="M0,444 C320,480 720,452 1200,378 L1200,695 L0,695 Z" fill="url(#steelFill)"/>
      <path d="M0,472 C340,512 760,480 1200,408 L1200,695 L0,695 Z" fill="var(--silver-mid)" opacity="0.55"/>
      <path d="M0,495 C360,535 780,502 1200,432 L1200,695 L0,695 Z" fill="url(#carbonFill)"/>
    </svg>

    <h1 class="card__name">Martin Colvey</h1>
    <p class="card__role">CEO</p>

    <ul class="card__contacts">
      <li>222222, Moscow, Ulitsa Tikhvoronskaya, 7B</li>
      <li>colvey@tessarine-mail.ru</li>
      <li>www.t38-studio.ru</li>
      <li>+7 (222) 222-22-22</li>
      <li>+7 (222) 222-22-22</li>
    </ul>

    <p class="card__brand">T38</p>
  </div>
</body>
</html>
```